Design marketing/advertisement email for consulting business

Hello - My company, Brindle-Oakes, is looking for a marketing professional to compose a "marketing" email to be sent to potential professional referral sources. The email should provide an introduction of our company's capabilities and services. We want this marketing piece to invite the recipient to schedule a call with us to further discuss how we could best work together. The email must included elements of our brand. Our website is www.brindleoakes-example.com and will provide you with all the details about our business as well as our logo, branding, contact details etc. Thanks so much!
Industry/Entity Type
Business

```html
<!DOCTYPE html>
<html lang="en">
<head>
<meta charset="utf-8">
<title>Brindle-Oakes – Senior Housing Consulting</title>
<link href="https://fonts.googleapis.com/css2?family=Arimo:wght@400&family=Tinos:ital@1&display=swap" rel="stylesheet">
<style>
  :root{
    --page:#e6dcd3;
    --coral:#e57b5e;
    --peach:#f9c29a;
    --slate:#393a42;
    --ink:#111111;
    --white:#ffffff;
    --sans:"Arimo", Arial, sans-serif;
    --serif:"Tinos", "Times New Roman", serif;
  }
  *{box-sizing:border-box;margin:0;padding:0}
  html,body{width:1200px;height:1200px;overflow:hidden;background:var(--page)}
  .flyer{position:absolute;left:241px;top:151px;width:720px;height:900px;background:var(--coral);border:1px solid #000;overflow:hidden;font-family:var(--sans)}
  .brand{position:absolute;left:40px;top:35px;display:flex;align-items:center;gap:14px}
  .brand-square{width:60px;height:60px;background:var(--slate)}
  .brand-name{font-family:var(--sans);font-size:34px;color:var(--slate);letter-spacing:0.5px}
  .intro{position:absolute;left:32px;top:142px;width:401px;font-family:var(--serif);font-style:italic;font-size:20px;line-height:27px;color:var(--white);text-align:justify;hyphens:auto;-webkit-hyphens:auto}
  .intro .lead{font-size:44px;line-height:20px;margin-left:80px}
  .contact{position:absolute;height:29px;background:var(--peach);display:flex;align-items:center;gap:12px;padding-left:10px;font-size:19px;color:var(--ink);white-space:nowrap}
  .contact svg{flex:none}
  .contact-phone{left:29px;top:562px;width:194px}
  .contact-fax{left:241px;top:562px;width:196px}
  .contact-email{left:55px;top:606px;width:356px;font-size:18px;justify-content:center;padding-left:0}
  .services{position:absolute;left:456px;top:138px;width:235px;height:493px;background:var(--peach);padding:0 7px}
  .services-title{height:76px;display:flex;align-items:center;justify-content:center;font-size:22px;font-weight:400;color:var(--ink);letter-spacing:0.5px}
  .service{height:132px;margin-bottom:7px;background:var(--slate);color:var(--white);display:flex;flex-direction:column;align-items:center;justify-content:center;text-align:center}
  .service h3{font-weight:400;font-size:29px;margin-bottom:8px}
  .service p{font-size:16.5px;line-height:21px}
  .office{position:absolute;top:670px;display:flex;gap:6px;font-size:16.5px;line-height:21.6px;color:var(--ink);font-style:normal;z-index:2;white-space:nowrap}
  .office-austin{left:30px}
  .office-paloalto{left:358px}
  .office svg{flex:none}
  .skyline{position:absolute;left:47px;top:690px;width:673px;height:210px;background:radial-gradient(ellipse at 55% 95%, #fff6d8 0%, #ffd59a 25%, #f79a72 55%, rgba(229,123,94,0) 80%)}
</style>
</head>
<body>
<div class="flyer">
  <div class="brand">
    <div class="brand-square"></div>
    <span class="brand-name">Brindle-Oakes</span>
  </div>

  <p class="intro"><span class="lead">B</span>rindle-Oakes was established to provide senior housing expertise to the real estate investment and development communities. Founded in 2011, Brindle-Oakes offers consulting services to investors, developers and asset managers within the senior housing investment space. Drawing upon the extensive experience of the company’s principals, Maren Brindle and Julia Oakes, Brindle-Oakes is able to offer a wide array of services to ensure successful and profitable senior housing development projects and investments. Brindle-Oakes has offices in Austin, Texas and Palo Alto, California.</p>

  <div class="contact contact-phone">
    <svg width="24" height="20" viewBox="0 0 24 20" fill="none" stroke="#111" stroke-width="1.6"><path d="M2 6c0-3 4-4 10-4s10 1 10 4v2h-5V6H7v2H2z"/><path d="M6 9h12l3 9H3z"/><circle cx="12" cy="13.5" r="2.5"/></svg>
    <span>512.555.0148</span>
  </div>
  <div class="contact contact-fax">
    <svg width="22" height="22" viewBox="0 0 22 22" fill="none" stroke="#111" stroke-width="1.6"><rect x="5" y="2" width="12" height="8"/><rect x="2" y="10" width="18" height="10"/><path d="M6 14h10M6 17h10"/></svg>
    <span>512.555.0192</span>
  </div>
  <div class="contact contact-email">
    <svg width="24" height="16" viewBox="0 0 24 16" fill="none" stroke="#111" stroke-width="1.5"><rect x="1" y="1" width="22" height="14"/><path d="M1 1l11 8 11-8M1 15l8-7M23 15l-8-7"/></svg>
    <span>info@brindleoakes-example.com</span>
  </div>

  <section class="services">
    <h2 class="services-title">SERVICES</h2>
    <div class="service"><h3>Development</h3><p>Acquisition, Planning<br>and Design</p></div>
    <div class="service"><h3>Operation</h3><p>Audits and Assessments</p></div>
    <div class="service"><h3>Disposition</h3><p>Transition and<br>Exit Strategies</p></div>
  </section>

  <div class="skyline" role="img" aria-label="Glowing city skyline silhouette at sunset"></div>

  <address class="office office-austin">
    <svg width="16" height="24" viewBox="0 0 16 24"><path d="M8 1a7 7 0 0 0-7 7c0 5 7 15 7 15s7-10 7-15a7 7 0 0 0-7-7z" fill="#111"/><circle cx="8" cy="8" r="2.8" fill="#e57b5e"/></svg>
    <span>Brindle-Oakes Partners, LLC – Austin<br>1420 Cedar Ridge Blvd.<br>Suite 410-118<br>Austin, TX 78701</span>
  </address>
  <address class="office office-paloalto">
    <svg width="16" height="24" viewBox="0 0 16 24"><path d="M8 1a7 7 0 0 0-7 7c0 5 7 15 7 15s7-10 7-15a7 7 0 0 0-7-7z" fill="#111"/><circle cx="8" cy="8" r="2.8" fill="#e57b5e"/></svg>
    <span>Brindle-Oakes Partners, LLC – Palo Alto<br>418 Alder Avenue, #20410<br>Palo Alto, CA 94301</span>
  </address>
</div>
</body>
</html>
```